New cool to-go cup for BRISK Coffee

We are looking for a new cool design for our to-go cups in kraft paper (same style as the attached photo).

The idea:

We have three different cups sizes: 6oz, 8oz and 12oz. We call them “One-Sixty” (6oz), “Two-Forty” (8oz) and “Three-sixty” (12oz) (refers to the size in milliliters). We would like to include this in the cup design. Please see the attached sketch of the idea ("Design ideas - Front").

The backside of the cup should have the attached text and logo ("Design ideas - Back").

But other ideas are also very welcome too! Maybe just a simple cup with the logo.

Please keep the design very minimalistic. The more simple the better.

Target Market(s)

Young urban people

Industry/Entity Type

Coffee shop

Font styles to use
Sans Serif

Requirements
Must have
• Kraft paper cups

```html
<!DOCTYPE html>
<html lang="en">
<head>
<meta charset="utf-8">
<title>BRISK Coffee – Eight Ounce Cup Sleeve</title>
<link rel="stylesheet" href="https://fonts.googleapis.com/css2?family=Montserrat:wght@300;400;600;700&display=swap">
<style>
  :root {
    --backdrop: #d4c8b9;
    --backdrop-low: #e8e5e1;
    --kraft-light: #dcb081;
    --kraft-mid: #c9955f;
    --kraft-dark: #9a6a38;
    --ink: #3a2416;
  }
  * { box-sizing: border-box; margin: 0; padding: 0; }
  html, body {
    width: 720px;
    height: 1200px;
    overflow: hidden;
  }
  body {
    font-family: "Montserrat", sans-serif;
    color: var(--ink);
    background: var(--backdrop);
  }
  .variant {
    position: relative;
    width: 720px;
    height: 600px;
    background: linear-gradient(to bottom, var(--backdrop) 0%, var(--backdrop) 80%, var(--backdrop-low) 100%);
  }
  .sleeve {
    position: absolute;
    top: 216px;
    height: 288px;
    background: linear-gradient(to right, var(--kraft-light) 0%, var(--kraft-mid) 60%, var(--kraft-dark) 100%);
  }
  .sleeve--front { left: 109px; width: 256px; }
  .sleeve--back { left: 365px; width: 247px; }
  .sleeve > * {
    position: absolute;
    left: 0;
    right: 0;
    text-align: center;
    transform: translateY(-50%);
    white-space: nowrap;
  }
  .hashtag {
    font-size: 27px;
    letter-spacing: -0.3px;
    line-height: 1;
  }
  .hashtag strong { font-weight: 700; }
  .hashtag span { font-weight: 300; }
  .brand {
    display: flex;
    justify-content: center;
    align-items: center;
    gap: 6px;
    font-weight: 600;
    font-size: 12px;
    letter-spacing: 1px;
    text-transform: uppercase;
  }
  .brand-dot {
    width: 12px;
    height: 12px;
    border: 2px solid var(--ink);
    border-radius: 50%;
  }
  .brand--large { font-size: 15px; }
  .brand--large .brand-dot { width: 15px; height: 15px; }
  .back-story {
    font-size: 10.5px;
    font-weight: 400;
    line-height: 12.6px;
  }
  .back-web { font-size: 10.5px; font-weight: 700; }
  .back-social { font-size: 10.5px; font-weight: 400; }

  .sleeve--front .hashtag { top: 121px; }
  .sleeve--back .brand { top: 72px; }
  .sleeve--back .back-story { top: 137px; }
  .sleeve--back .back-web { top: 175px; }
  .sleeve--back .back-social { top: 200px; }
  .sleeve--front .brand--large { top: 108px; }
  .variant--logo-hashtag .sleeve--front .hashtag { top: 171px; }
</style>
</head>
<body>

  <section class="variant variant--hashtag">
    <div class="sleeve sleeve--front">
      <p class="hashtag"><strong>#eight</strong><span>ounce</span></p>
    </div>
    <div class="sleeve sleeve--back">
      <p class="brand"><span class="brand-dot"></span>BRISK Coffee</p>
      <p class="back-story">Read about your coffee<br>and the dedicated farmers<br>who made this cup possible:</p>
      <p class="back-web">www.briskbeanery.com</p>
      <p class="back-social">@briskbeanery</p>
    </div>
  </section>

  <section class="variant variant--logo-hashtag">
    <div class="sleeve sleeve--front">
      <p class="brand brand--large"><span class="brand-dot"></span>BRISK Coffee</p>
      <p class="hashtag"><strong>#eight</strong><span>ounce</span></p>
    </div>
    <div class="sleeve sleeve--back">
      <p class="brand"><span class="brand-dot"></span>BRISK Coffee</p>
      <p class="back-story">Read about your coffee<br>and the dedicated farmers<br>who made this cup possible:</p>
      <p class="back-web">www.briskbeanery.com</p>
      <p class="back-social">@briskbeanery</p>
    </div>
  </section>

</body>
</html>
```